One of Australia's fastest growing Financial Company looking for an updated business card design!

Meridale Holdings Australia is looking for an updated design for our business cards. We would like to keep up our professional appearances and have get new exciting design that fits our company.

The Meridale aim is to facilitate and assist clients in every financial requirement that may arise in financial areas.

We would to see the design to use colour blue and we like the clouds in the background. We have attached two designs we have use before but we need something with more professional and easy to read design.

We would like the website in the back of the card; the employees name more central and stands out; only a postal address; a list of all our locations along the bottom (Sydney, Melbourne, Brisbane, Singapore)

Looking forward to seeing the designs come in!

Target Market(s)

Other Industry Professionals
Middle Class Families

Industry/Entity Type

Finance

Contact Information for Business Card

Name; Company Role; Office Number; Mobile Number; Email Address; Website; Postal Address; Locations

Font styles to use
Serif
Sans Serif

Colors
0492cd
33a6d7
85cae6
85acd3
3176b5
0455a3
cee9f5
d5e2ee

Requirements
Must have
• Name; Company Role; Office Number; Mobile Number; Email Address; Website; Postal Address; Locations
Nice to have
• The colour blue, clouds on the background

```html
<!DOCTYPE html>
<html lang="en">
<head>
<meta charset="utf-8">
<title>Meridale Business Card</title>
<link rel="stylesheet" href="https://fonts.googleapis.com/css2?family=Noto+Serif:wght@400;700&display=swap">
<style>
  :root {
    --bg: #2a2b2e;
    --paper: #ffffff;
    --brand-blue: #1f7fcf;
    --ink-blue: #1f6fc0;
    --accent-red: #e0262b;
    --sky-deep: #1d96dc;
    --sky-mid: #33a6d7;
    --sky-light: #85cae6;
    --sky-pale: #cee9f5;
  }
  * { margin: 0; padding: 0; box-sizing: border-box; }
  html, body { width: 1200px; height: 900px; overflow: hidden; }
  body {
    background: var(--bg);
    font-family: "Noto Serif", Georgia, serif;
    display: flex;
    align-items: center;
    justify-content: center;
    gap: 50px;
  }
  .card {
    position: relative;
    width: 540px;
    height: 310px;
    border-radius: 22px;
    overflow: hidden;
  }
  /* Front */
  .card-front { background: var(--paper); }
  .brand-front {
    position: absolute;
    top: 34px;
    right: 36px;
    font-size: 56px;
    line-height: 1.2;
    font-weight: 700;
    color: var(--brand-blue);
    display: flex;
    align-items: center;
    gap: 12px;
  }
  .brand-mark {
    width: 32px; height: 32px;
    border-radius: 50%;
    background: currentColor;
    flex: none;
  }
  .person { position: absolute; top: 140px; left: 52px; }
  .person-name { color: var(--accent-red); font-size: 18px; font-weight: 700; letter-spacing: 0.5px; }
  .person-role { color: var(--ink-blue); font-size: 12px; margin-top: 4px; }
  .divider {
    position: absolute; top: 136px; left: 262px;
    width: 1px; height: 88px;
    background: linear-gradient(to bottom, transparent, var(--sky-light), transparent);
  }
  .contacts {
    position: absolute; top: 134px; left: 288px;
    list-style: none; color: var(--ink-blue); font-size: 13px;
  }
  .contacts li { display: flex; align-items: center; gap: 12px; height: 22px; }
  .contacts svg { width: 13px; height: 13px; flex: none; }
  .address {
    position: absolute; top: 236px; left: 52px;
    color: var(--ink-blue); font-size: 12px;
  }
  .locations {
    position: absolute; top: 262px; left: 52px; right: 36px;
    list-style: none; display: flex; gap: 18px;
    color: var(--accent-red); font-size: 11px; font-weight: 700;
    letter-spacing: 1.2px; text-transform: uppercase;
  }
  .edge-band {
    position: absolute; left: 0; bottom: 0;
    width: 100%; height: 16px;
  }
  /* Back */
  .card-back {
    background: linear-gradient(160deg, var(--sky-deep) 0%, var(--sky-mid) 45%, var(--sky-deep) 100%);
  }
  .clouds {
    position: absolute; inset: 0;
    background:
      radial-gradient(ellipse 140px 60px at 30% 22%, rgba(255,255,255,0.55), transparent 70%),
      radial-gradient(ellipse 170px 70px at 72% 78%, rgba(255,255,255,0.5), transparent 70%),
      radial-gradient(ellipse 120px 50px at 50% 48%, rgba(206,233,245,0.4), transparent 70%);
  }
  .brand-back {
    position: absolute; top: 118px; left: 0; right: 0;
    justify-content: center;
    font-size: 60px; line-height: 1.2; font-weight: 700; color: var(--paper);
    display: flex; align-items: center; gap: 12px;
  }
  .back-website {
    position: absolute; bottom: 32px; left: 0; right: 0;
    text-align: center; color: var(--paper);
    font-size: 15px; letter-spacing: 1px;
  }
</style>
</head>
<body>
  <section class="card card-front">
    <div class="brand-front"><span class="brand-mark"></span>Meridale</div>

    <div class="person">
      <p class="person-name">JOHN SMITH</p>
      <p class="person-role">Managing Director</p>
    </div>

    <div class="divider"></div>

    <ul class="contacts">
      <li>
        <svg viewBox="0 0 14 14"><path d="M3 1 L5 1 L6 4 L4.5 5 Q5.5 8 9 9.5 L10 8 L13 9 L13 11 Q12 13 10 13 Q2 11 1 3 Q1 1 3 1Z" fill="var(--accent-red)"/></svg>
        Office (123) 45678 90
      </li>
      <li>
        <svg viewBox="0 0 14 14"><rect x="3.5" y="1" width="7" height="12" rx="1.5" fill="var(--accent-red)"/><rect x="4.7" y="2.6" width="4.6" height="7.4" fill="#fff"/><circle cx="7" cy="11.5" r="0.7" fill="#fff"/></svg>
        Mobile 0412 345 678
      </li>
      <li>
        <svg viewBox="0 0 14 14"><rect x="1" y="3" width="12" height="8" fill="var(--accent-red)"/><path d="M1 3 L7 8 L13 3" stroke="#fff" stroke-width="1" fill="none"/></svg>
        info@domain.com
      </li>
      <li>
        <svg viewBox="0 0 14 14"><circle cx="7" cy="7" r="6" fill="var(--accent-red)"/><path d="M1 7 H13 M7 1 Q4 7 7 13 M7 1 Q10 7 7 13" stroke="#fff" stroke-width="0.8" fill="none"/></svg>
        www.website.com
      </li>
    </ul>

    <p class="address">PO Box 123, Town Here, City Name 123456</p>

    <ul class="locations">
      <li>Sydney</li>
      <li>Melbourne</li>
      <li>Brisbane</li>
      <li>Singapore</li>
    </ul>

    <svg class="edge-band" viewBox="0 0 540 16" preserveAspectRatio="none">
      <rect x="0" y="0" width="540" height="16" fill="var(--sky-mid)"/>
      <polygon points="0,0 240,0 228,16 0,16" fill="var(--accent-red)"/>
    </svg>
  </section>

  <section class="card card-back">
    <div class="clouds" role="img" aria-label="Soft white clouds across a blue sky"></div>
    <div class="brand-back"><span class="brand-mark"></span>Meridale</div>
    <p class="back-website">www.website.com</p>
  </section>
</body>
</html>
```